Vantrel Telecom Corporate Website & Social Branding

We are looking for a new website for our startup telecom which provides UCaaS, SD-WAN, Business SMS/MMS, Video Conferencing, Managed Network Service & more.

Target Market(s)

Small offices from 1-250 users

Industry/Entity Type

Telecomunications

Coding

Coded - Design and coding required

Colors
0054AA
0677BA
7BADD7
CADEEF
E8F1F8

```html
<!DOCTYPE html>
<html lang="en">
<head>
<meta charset="utf-8">
<title>Vantrel Telecom</title>
<link href="https://fonts.googleapis.com/css2?family=Poppins:wght@500;600;700&family=Work+Sans:wght@400;500;600&display=swap" rel="stylesheet">
<style>
:root{
  --navy:#0054AA;
  --blue:#0677BA;
  --sky:#7BADD7;
  --mist:#CADEEF;
  --ice:#E8F1F8;
  --ink:#1b1b1f;
  --text:#4a4d55;
  --white:#ffffff;
  --green:#1fbf6a;
  --red:#f04b4b;
}
*{margin:0;padding:0;box-sizing:border-box}
html,body{width:1200px;height:3538px;overflow:hidden;background:var(--white)}
body{position:relative;font-family:"Work Sans",sans-serif;color:var(--text)}
.abs{position:absolute}
h1,h2,h3{font-family:"Poppins",sans-serif;color:var(--ink)}
.eyebrow{font-family:"Poppins",sans-serif;font-weight:600;color:var(--blue);font-size:21px;letter-spacing:.5px}
.btn{position:absolute;display:flex;align-items:center;justify-content:center;background:var(--blue);color:var(--white);font-family:"Poppins",sans-serif;font-weight:600;font-size:15px;border-radius:4px;box-shadow:0 6px 14px rgba(6,119,186,.3)}
.brand{display:flex;align-items:center;gap:10px;font-family:"Poppins",sans-serif;font-weight:600;font-size:22px;color:var(--ink)}
.brand .dot{width:30px;height:30px;border-radius:50%;background:var(--blue)}

/* nav */
.nav a{position:absolute;top:29px;font-size:14px;color:var(--ink);text-decoration:none;font-weight:500}
.nav .try{top:16px;left:953px;width:141px;height:43px;border:1.5px solid var(--blue);border-radius:4px;color:var(--blue);display:flex;align-items:center;justify-content:center;font-family:"Poppins",sans-serif;font-weight:600;font-size:15px}

/* hero */
.hero{left:43px;top:74px;width:1114px;height:486px;border-radius:22px;background:linear-gradient(90deg,#e7eefb,#dfe9fb);overflow:hidden}
.hero-title{left:104px;top:188px;font-size:41px;line-height:57px;font-weight:600;white-space:nowrap}
.hero-title .mark{background:linear-gradient(transparent 78%,#55c2ef 78%,#55c2ef 92%,transparent 92%)}
.hero-copy{left:106px;top:303px;width:470px;font-size:15px;line-height:21px;color:var(--ink)}
.rating{left:106px;top:457px}
.rating .lbl{font-size:15px;color:var(--ink);font-weight:500}
.stars{display:flex;gap:2px;margin-top:4px}
.stars span{width:16px;height:16px;background:#00b67a}
.rating .based{font-size:9px;color:var(--ink);margin-top:5px}
.rating .based u{color:var(--blue)}
.rating .rv{display:flex;align-items:center;gap:4px;font-size:12px;color:var(--ink);margin-top:4px}
.rating .rv i{width:11px;height:11px;background:#00b67a;display:block}

.call{left:640px;top:128px;width:391px;height:384px;border-radius:28px;background:var(--white);box-shadow:0 10px 30px rgba(0,84,170,.18);padding:5px}
.call .screen{width:381px;height:320px;border-radius:24px 24px 0 0;background:linear-gradient(160deg,#d9d4cc,#c8a274 55%,#8d6a4a);position:relative}
.call .caption{position:absolute;left:56px;bottom:16px;width:275px;height:24px;border-radius:5px;background:var(--white);font-size:7.5px;color:var(--ink);display:flex;align-items:center;justify-content:center}
.ctrls{position:absolute;left:18px;top:339px;width:355px;height:34px;display:flex;align-items:center;gap:8px}
.vol{width:110px;height:34px;border-radius:8px;background:var(--ice);display:flex;align-items:center;padding:0 10px;gap:6px}
.vol .bar{flex:1;height:3px;background:var(--mist);position:relative}
.vol .bar b{position:absolute;left:0;top:0;width:60%;height:3px;background:var(--green)}
.ctl{width:34px;height:34px;border-radius:8px;background:#eef2f7;display:flex;align-items:center;justify-content:center}
.ctl.cc{background:#15b35e;color:#fff;font-family:"Poppins",sans-serif;font-weight:600;font-size:13px}
.thumb{border-radius:12px;border:4px solid var(--white);box-shadow:0 6px 16px rgba(0,0,0,.15)}
.thumb .tag{position:absolute;left:8px;bottom:6px;font-size:9px;color:var(--white);font-weight:600}
.thumb .badge{position:absolute;right:-10px;bottom:-10px;width:22px;height:22px;border-radius:50%;border:2px solid #fff}

/* solution */
.portrait{left:150px;top:650px;width:390px;height:410px;border-radius:50%;background:linear-gradient(170deg,#8a5a3c 0%,#e2b99a 40%,#f1ede8 75%,#cfe3f2 100%)}
.feat{left:611px;width:520px}
.feat .ic{position:absolute;left:0;top:0;width:62px;height:62px;border-radius:50%;box-shadow:0 8px 16px rgba(0,0,0,.08);display:flex;align-items:center;justify-content:center}
.feat h3{position:absolute;left:79px;top:0;font-size:17px;font-weight:600}
.feat p{position:absolute;left:81px;top:24px;width:400px;font-size:13.5px;line-height:20px}

/* services */
.card{position:absolute;width:315px;height:195px;background:var(--white);border:2px solid #eef0f3;border-radius:8px;box-shadow:0 6px 18px rgba(0,0,0,.05);text-align:center}
.card.active{border-bottom:4px solid var(--blue)}
.card h3{display:flex;align-items:center;justify-content:center;gap:10px;font-size:17px;font-weight:600;margin-top:44px}
.card p{width:240px;margin:14px auto 0;font-size:13.5px;line-height:19.5px}

/* cta */
.trial{left:104px;top:1882px;width:990px;height:294px;border-radius:12px;background:linear-gradient(115deg,#2fb49a 0%,#3aa3c9 45%,#4b86e8 100%);text-align:center;color:var(--white);overflow:hidden}
.trial h2{color:var(--white);font-size:29px;line-height:34px;font-weight:600;margin-top:55px}
.trial p{font-size:13.5px;line-height:20px;margin-top:10px;opacity:.92}
.field{position:absolute;top:197px;height:42px;background:#fff;border-radius:3px;color:#666;font-size:13px;display:flex;align-items:center;padding-left:13px;text-align:left}
.trial .go{position:absolute;left:647px;top:197px;width:144px;height:42px;background:var(--blue);border:2px solid #fff;border-radius:4px;font-family:"Poppins",sans-serif;font-weight:600;font-size:15px;display:flex;align-items:center;justify-content:center}

/* assistant */
.device-photo{left:570px;top:2250px;width:630px;height:395px;border-radius:55% 0 50% 50% / 45% 0 55% 55%;background:linear-gradient(150deg,#2a2d33 0%,#8d8f95 30%,#e6e0d8 55%,#c69a72 75%,#0a86c8 100%)}

/* crm */
.logos{left:0;top:2884px;width:1200px;height:44px}
.logos span{position:absolute;top:0;transform:translateX(-50%);font-family:"Poppins",sans-serif;font-weight:600;font-size:22px;color:#2d2f36;display:flex;align-items:center;gap:8px;white-space:nowrap}
.logos span i{width:18px;height:18px;border-radius:50%;background:var(--blue);display:block}

/* banner */
.banner{left:104px;top:3003px;width:990px;height:189px;border-radius:14px;background:var(--blue)}
.banner .circ{position:absolute;left:30px;top:46px;width:96px;height:96px;border-radius:50%;background:rgba(255,255,255,.12);display:flex;align-items:center;justify-content:center}
.banner .circ div{width:70px;height:70px;border-radius:50%;background:rgba(255,255,255,.18);display:flex;align-items:center;justify-content:center}
.banner p{position:absolute;left:154px;top:66px;width:600px;font-family:"Poppins",sans-serif;font-weight:600;font-size:21px;line-height:29px;color:#fff}
.banner .dark{position:absolute;left:788px;top:72px;width:143px;height:44px;background:#0b0b0b;color:#fff;border-radius:4px;font-family:"Poppins",sans-serif;font-weight:600;font-size:15px;display:flex;align-items:center;justify-content:center}

/* footer */
.fcol h4{font-family:"Poppins",sans-serif;font-weight:600;font-size:14px;color:var(--ink)}
.fcol li{list-style:none;font-size:13.5px;color:var(--ink)}
.social li{display:flex;align-items:center;gap:10px}
.social li i{width:22px;height:22px;border-radius:50%;background:var(--blue);display:block}
.copy{left:0;top:3500px;width:1200px;text-align:center;font-size:11.5px;color:var(--ink)}
.copy a{color:var(--blue)}
</style>
</head>
<body>

<header class="nav">
  <div class="abs brand" style="left:106px;top:20px"><span class="dot"></span>Vantrel Telecom</div>
  <a style="left:553px">Home</a>
  <a style="left:621px">Solutions</a>
  <a style="left:711px">Products</a>
  <a style="left:800px">Pricing</a>
  <a style="left:874px">&#128274;&#xFE0E; Login</a>
  <a class="try">Try for FREE</a>
</header>

<section class="abs hero">
  <svg class="abs" style="left:0;top:0" width="1114" height="486" aria-hidden="true">
    <g fill="none" stroke="#bcd3f2" stroke-width="1.5">
      <circle cx="781" cy="256" r="200"/><circle cx="781" cy="256" r="240"/><circle cx="781" cy="256" r="280"/>
    </g>
  </svg>
</section>
<h1 class="abs hero-title"><span class="mark">Expanded opportunities</span><br>for remote work</h1>
<p class="abs hero-copy">Massa, molestie amet, non, mattis viverra gravida elit vestibulum augue. Morbi in risus nibh tellus diam vitae at.</p>
<a class="btn" style="left:106px;top:367px;width:142px;height:42px">Get Started</a>
<div class="abs rating">
  <div class="lbl">Excellent</div>
  <div class="stars"><span></span><span></span><span></span><span></span><span></span></div>
  <div class="based">Based on <u>628 reviews</u></div>
  <div class="rv"><i></i>Reviewly</div>
</div>

<div class="abs call">
  <div class="screen" role="img" aria-label="Video call photo of a man with a headset waving">
    <div class="caption">Hello guys... Yesterday we discuss about Management Project and...</div>
  </div>
  <div class="ctrls">
    <div class="vol"><svg width="10" height="10"><path d="M1 3h3l3-2v8L4 7H1z" fill="#1fbf6a"/></svg><div class="bar"><b></b></div></div>
    <div style="flex:1"></div>
    <div class="ctl"><svg width="12" height="14" fill="none" stroke="#9aa3ad" stroke-width="1.5"><rect x="4" y="1" width="4" height="8" rx="2"/><path d="M2 7a4 4 0 0 0 8 0M6 11v2"/></svg></div>
    <div class="ctl"><svg width="16" height="12" fill="none" stroke="#9aa3ad" stroke-width="1.5"><rect x="1" y="2" width="10" height="8" rx="1"/><path d="M11 5l4-2v6l-4-2"/></svg></div>
    <div class="ctl"><svg width="12" height="12" fill="#9aa3ad"><rect x="1" y="1" width="4" height="10"/><rect x="7" y="1" width="4" height="4"/></svg></div>
    <div class="ctl cc">CC</div>
    <div class="ctl"><svg width="12" height="12" fill="none" stroke="#9aa3ad" stroke-width="1.5"><path d="M1 4V1h3M8 1h3v3M11 8v3H8M4 11H1V8"/></svg></div>
  </div>
</div>
<div class="abs thumb" style="left:1038px;top:128px;width:67px;height:68px;background:linear-gradient(150deg,#f3c6a7,#c4493d)" role="img" aria-label="Participant photo"><span class="tag">Lena</span><span class="badge" style="background:var(--red)"></span></div>
<div class="abs thumb" style="left:997px;top:295px;width:88px;height:89px;background:linear-gradient(160deg,#e9edf1,#b4c0a2)" role="img" aria-label="Participant photo"><span class="tag">You</span><span class="badge" style="background:var(--green)"></span></div>
<div class="abs thumb" style="left:509px;top:390px;width:88px;height:90px;background:linear-gradient(160deg,#d9c7b3,#4a7fb8)" role="img" aria-label="Participant photo"><span class="tag">Dana</span><span class="badge" style="background:var(--red)"></span></div>

<div class="abs portrait" role="img" aria-label="Photo of a smiling woman holding a phone with the Vantrel app"></div>
<div class="abs eyebrow" style="left:612px;top:631px">Meet Your New</div>
<h2 class="abs" style="left:612px;top:659px;font-size:36px;font-weight:600">Communication Solution</h2>
<p class="abs" style="left:612px;top:713px;width:420px;font-size:13.5px;line-height:20px">Lorem ipsum dolor sit amet, consectetur adipiscing elit. Faucibus enim ornare scelerisque nibh purus.</p>

<div class="abs feat" style="top:799px">
  <div class="ic" style="background:#e4f7ee"><svg width="24" height="20" fill="none" stroke="#1fbf6a" stroke-width="1.8"><rect x="1" y="1" width="22" height="14" rx="2"/><path d="M5 5h2M10 5h2M15 5h2M5 9h2M10 9h2M15 9h2M8 19h8"/></svg></div>
  <h3>Powerful, easy to use software</h3>
  <p>Lorem ipsum dolor sit amet, consectetur adipiscing elit aucibus enim.</p>
</div>
<div class="abs feat" style="top:891px">
  <div class="ic" style="background:#e6f1fb"><svg width="24" height="24" fill="none" stroke="#1a8fd0" stroke-width="1.8"><circle cx="10" cy="10" r="7"/><path d="M15 15l7 7M6 13l8-7"/></svg></div>
  <h3>No contracts. No hidden fees</h3>
  <p>Lorem ipsum dolor sit amet, consectetur adipiscing elit aucibus enim. Tristique imperdiet metus, risus nunc quis.</p>
</div>
<div class="abs feat" style="top:982px">
  <div class="ic" style="background:#fdf4e0"><svg width="24" height="24" fill="none" stroke="#f3b63a" stroke-width="1.8"><circle cx="12" cy="12" r="5"/><circle cx="12" cy="12" r="10" stroke-dasharray="3 3"/></svg></div>
  <h3>Awesome customer service</h3>
  <p>Lorem ipsum dolor sit amet, consectetur adipiscing elit aucibus enim .</p>
</div>

<div class="abs eyebrow" style="left:0;top:1200px;width:1200px;text-align:center">We Provide</div>
<h2 class="abs" style="left:0;top:1226px;width:1200px;text-align:center;font-size:36px;font-weight:600">Powerful Services</h2>

<div class="card" style="left:104px;top:1307px">
  <h3><svg width="26" height="26" fill="none" stroke="#1a8fd0" stroke-width="1.6"><circle cx="13" cy="8" r="5"/><path d="M3 24c0-6 4-9 10-9s10 3 10 9M4 10a3 3 0 0 1 0-5M22 10a3 3 0 0 0 0-5"/></svg>UCaaS</h3>
  <p>Lorem ipsum dolor sit amet, consectetur adipiscing elit aucibus enim. Tristique imperdiet metus, risus nunc quis.</p>
</div>
<div class="card active" style="left:442px;top:1307px">
  <h3><svg width="26" height="26" fill="none" stroke="#1a8fd0" stroke-width="1.6"><circle cx="13" cy="11" r="9"/><path d="M4 11h18M13 2c-4 5-4 13 0 18M13 2c4 5 4 13 0 18M8 24h10"/></svg>SD-WAN</h3>
  <p>Lorem ipsum dolor sit amet, consectetur adipiscing elit aucibus enim. Tristique imperdiet metus, risus nunc quis.</p>
</div>
<div class="card" style="left:781px;top:1307px">
  <h3><svg width="26" height="26" fill="none" stroke="#1a8fd0" stroke-width="1.6"><rect x="2" y="3" width="16" height="11" rx="2"/><rect x="12" y="6" width="11" height="18" rx="2"/><path d="M6 14l-2 4 5-4"/></svg>Business SMS/MMS</h3>
  <p>Lorem ipsum dolor sit amet, consectetur adipiscing elit aucibus enim. Tristique imperdiet metus, risus nunc quis.</p>
</div>
<div class="card" style="left:275px;top:1527px">
  <h3><svg width="26" height="26" fill="none" stroke="#1a8fd0" stroke-width="1.6"><rect x="2" y="2" width="22" height="16" rx="2"/><circle cx="13" cy="8" r="3"/><path d="M8 16c1-3 9-3 10 0M9 24h8M13 18v6"/></svg>Video Conferencing</h3>
  <p>Lorem ipsum dolor sit amet, consectetur adipiscing elit aucibus enim. Tristique imperdiet metus, risus nunc quis.</p>
</div>
<div class="card" style="left:612px;top:1527px">
  <h3><svg width="28" height="26" fill="none" stroke="#1a8fd0" stroke-width="1.6"><path d="M7 17a6 6 0 0 1 1-12 7 7 0 0 1 13 2 5 5 0 0 1 0 10"/><path d="M14 11v13M10 24h8M14 15l-4-3M14 15l4-3"/></svg>Managed Network Service</h3>
  <p>Lorem ipsum dolor sit amet, consectetur adipiscing elit aucibus enim. Tristique imperdiet metus, risus nunc quis.</p>
</div>
<a class="btn" style="left:529px;top:1759px;width:142px;height:42px">All Services</a>

<section class="abs trial">
  <h2>DO YOU WANT TO TRY ALL THE CONVENIENCES<br>OF THE SERVICES?</h2>
  <p>Lorem ipsum dolor sit amet, consectetur adipiscing elit aucibus enim.<br>Tristique imperdiet metus, risus nunc quis.</p>
  <div class="field" style="left:201px;width:167px">Company name</div>
  <div class="field" style="left:378px;width:261px">Email address</div>
  <div class="go">Try for FREE</div>
</section>

<div class="abs eyebrow" style="left:106px;top:2318px">Dolor Sit Amet</div>
<h2 class="abs" style="left:106px;top:2346px;font-size:36px;font-weight:600">Your Helpful Assistant</h2>
<p class="abs" style="left:106px;top:2422px;width:420px;font-size:13.5px;line-height:20px;color:var(--ink)">Diam quis viverra tincidunt velit eu felis hendrerit in convallis. Blandit velit lorem integer consectetur. Pretium donec malesuada quis ac ultricies ac. Sagittis hac eget vitae, risus, vel velit sit tempus bibendum. Quis ac duis interdum curabitur. Massa, molestie amet, non, mattis viverra gravida elit vestibulum augue.</p>
<a class="btn" style="left:106px;top:2562px;width:162px;height:43px">Find Out More</a>
<div class="abs device-photo" role="img" aria-label="Photo of a laptop showing a video meeting, a phone in hand and a coffee cup"></div>

<div class="abs eyebrow" style="left:0;top:2780px;width:1166px;text-align:center">Integrate your favourite</div>
<h2 class="abs" style="left:0;top:2806px;width:1166px;text-align:center;font-size:36px;font-weight:600">CRM &amp; Helpdesk</h2>
<div class="abs logos">
  <span style="left:150px"><i></i>Skyledger</span>
  <span style="left:283px">Hubnest</span>
  <span style="left:446px">Zentro</span>
  <span style="left:612px">Chatterly</span>
  <span style="left:763px">Deskwise</span>
  <span style="left:925px">Flowdeal</span>
  <span style="left:1066px">Talkhub</span>
</div>

<section class="abs banner">
  <div class="circ"><div><svg width="30" height="28" fill="#fff"><rect x="1" y="12" width="6" height="14" rx="1"/><path d="M9 12l6-10c3 0 4 2 3 5l-1 4h8c2 0 3 2 2 4l-3 10c-1 1-2 2-3 2H9z"/></svg></div></div>
  <p>Lorem ipsum dolor sit amet, consectetur adipiscing elit aucibus enim. Tristique imperdiet metus</p>
  <div class="dark">Get Started</div>
</section>

<footer>
  <div class="abs brand" style="left:106px;top:3280px"><span class="dot"></span>Vantrel Telecom</div>
  <p class="abs" style="left:104px;top:3321px;width:240px;font-size:13.5px;line-height:19.5px">Lorem ipsum dolor sit amet, consectetur adipiscing elit aucibus enim. Tristique imperdiet metus, risus nunc quis.</p>
  <div class="abs fcol" style="left:512px;top:3276px">
    <h4>QUICK LINKS</h4>
    <ul style="margin-top:20px;line-height:28.5px"><li>Solutions</li><li>Products</li><li>Pricing</li><li>Login</li></ul>
  </div>
  <div class="abs fcol" style="left:718px;top:3276px">
    <h4>SERVICES</h4>
    <ul style="margin-top:20px;line-height:26.7px"><li>UCaaS</li><li>SD-WAN</li><li>Business SMS/MMS</li><li>Video Conferencing</li><li>Managed Network Service</li></ul>
  </div>
  <div class="abs fcol social" style="left:986px;top:3276px">
    <h4>SOCIAL MEDIA</h4>
    <ul style="margin-top:17px"><li style="height:36px"><i></i>Flitter</li><li style="height:36px"><i></i>Workline</li><li style="height:36px"><i></i>Friendsy</li><li style="height:36px"><i></i>Viewtube</li></ul>
  </div>
  <div class="abs copy">©Copyright 2022. <a>Vantrel TELECOM</a> | All Rights Reserved</div>
</footer>

</body>
</html>
```